Corporate Business Card

Very professional, Modern, Not to busy, include phone address email, website
(253) 555-0174, 61807 19th Street N, Fernmoor, OR 98517, marcus@kestrelbayholding.com, brelvanindustries.com

Target Market(s)

Manufacturing

Industry/Entity Type

Aero, machining, manufacturing, Off road racing

Contact Information for Business Card

Phone, address email, website

```html
<!DOCTYPE html>
<html lang="en">
<head>
<meta charset="utf-8">
<title>Brelvan Industries — Business Card</title>
<link rel="stylesheet" href="https://fonts.googleapis.com/css2?family=Oswald:wght@300;400;600&display=swap">
<style>
  :root {
    --backdrop: #dfe0e3;
    --card-red-light: #e3202b;
    --card-red: #b8050f;
    --card-red-dark: #7c0006;
    --paper: #ffffff;
    --navy: #1c3578;
    --ink-grey: #55585e;
    --white: #ffffff;
  }
  * { margin: 0; padding: 0; box-sizing: border-box; }
  html, body {
    width: 1200px;
    height: 800px;
    overflow: hidden;
    background: var(--backdrop);
    font-family: "Oswald", "Arial Narrow", sans-serif;
  }
  .card-sheet {
    position: relative;
    width: 1200px;
    height: 800px;
  }
  .card {
    position: absolute;
    top: 257px;
    width: 500px;
    height: 286px;
    box-shadow: 0 10px 28px rgba(0,0,0,0.18);
  }
  .card-front {
    left: 70px;
    background: radial-gradient(ellipse at 62% 38%, var(--card-red-light) 0%, var(--card-red) 45%, var(--card-red-dark) 100%);
    display: flex;
    align-items: center;
    justify-content: center;
  }
  .card-back {
    left: 630px;
    background: var(--paper);
  }
  .wordmark {
    text-align: center;
    font-weight: 600;
    text-transform: uppercase;
    line-height: 1;
  }
  .wordmark-name { font-size: 54px; letter-spacing: 3px; display: block; }
  .wordmark-sub { font-size: 20px; letter-spacing: 6px; display: block; margin-top: 6px; }
  .card-front .wordmark { color: var(--white); }
  .card-back .wordmark {
    position: absolute;
    right: 34px;
    bottom: 34px;
    color: var(--navy);
    text-align: right;
  }
  .card-back .wordmark-name { font-size: 44px; }
  .card-back .wordmark-sub { font-size: 16px; letter-spacing: 5px; }
  .contact-list {
    list-style: none;
    position: absolute;
    left: 30px;
    top: 28px;
  }
  .contact-item {
    display: flex;
    align-items: center;
    gap: 8px;
    font-weight: 300;
    font-size: 15px;
    color: var(--ink-grey);
    line-height: 24px;
    letter-spacing: 0.3px;
  }
  .contact-icon { width: 12px; height: 12px; fill: var(--navy); flex: none; }
</style>
</head>
<body>
<main class="card-sheet">
  <section class="card card-front" aria-label="Card front">
    <p class="wordmark">
      <span class="wordmark-name">Brelvan</span>
      <span class="wordmark-sub">Industries</span>
    </p>
  </section>

  <section class="card card-back" aria-label="Card back">
    <ul class="contact-list">
      <li class="contact-item">
        <svg class="contact-icon" viewBox="0 0 24 24" aria-hidden="true"><path d="M6.6 10.8a15 15 0 0 0 6.6 6.6l2.2-2.2c.3-.3.7-.4 1-.2 1.1.4 2.3.6 3.6.6.6 0 1 .4 1 1V20c0 .6-.4 1-1 1C10.6 21 3 13.4 3 4c0-.6.4-1 1-1h3.5c.6 0 1 .4 1 1 0 1.3.2 2.5.6 3.6.1.3 0 .7-.2 1z"/></svg>
        (541) 555-0174
      </li>
      <li class="contact-item">
        <svg class="contact-icon" viewBox="0 0 24 24" aria-hidden="true"><path d="M12 2a10 10 0 1 0 0 20 10 10 0 0 0 0-20zm6.9 6h-3a15 15 0 0 0-1.3-3.9A8 8 0 0 1 18.9 8zM12 4c.8 1.2 1.5 2.5 1.9 4h-3.8c.4-1.5 1.1-2.8 1.900-4zM4.3 14a8 8 0 0 1 0-4h3.4a16 16 0 0 0 0 4zm.8 2h3a15 15 0 0 0 1.3 3.9A8 8 0 0 1 5.1 16zm3-8h-3a8 8 0 0 1 4.3-3.9C8.8 5.3 8.4 6.6 8.1 8zM12 20c-.8-1.2-1.5-2.5-1.9-4h3.8c-.4 1.5-1.1 2.8-1.9 4zm2.3-6H9.7a14 14 0 0 1 0-4h4.6a14 14 0 0 1 0 4zm.3 5.9c.6-1.2 1-2.5 1.3-3.9h3a8 8 0 0 1-4.3 3.9zm1.7-5.9a16 16 0 0 0 0-4h3.4a8 8 0 0 1 0 4z"/></svg>
        www.brelvanindustries.com
      </li>
      <li class="contact-item">
        <svg class="contact-icon" viewBox="0 0 24 24" aria-hidden="true"><path d="M3 5h18c.6 0 1 .4 1 1v12c0 .6-.4 1-1 1H3c-.6 0-1-.4-1-1V6c0-.6.4-1 1-1zm9 7.5L20 7H4z"/></svg>
        marcus@kestrelbayholding.com
      </li>
      <li class="contact-item">
        <svg class="contact-icon" viewBox="0 0 24 24" aria-hidden="true"><path d="M12 2a7 7 0 0 0-7 7c0 5.2 7 13 7 13s7-7.8 7-13a7 7 0 0 0-7-7zm0 9.5a2.5 2.5 0 1 1 0-5 2.5 2.5 0 0 1 0 5z"/></svg>
        61807 19th Street N. Fernmoor, OR 98517
      </li>
    </ul>
    <p class="wordmark">
      <span class="wordmark-name">Brelvan</span>
      <span class="wordmark-sub">Industries</span>
    </p>
  </section>
</main>
</body>
</html>
```